Job advertisement

A graphic job advertisement. It's supposed to be slightly different from the normal ads. Eye-catcher and later the text for the job description.

```html
<!DOCTYPE html>
<html lang="de">
<head>
<meta charset="utf-8">
<title>Stellenanzeige – Power Worker</title>
<link rel="stylesheet" href="https://fonts.googleapis.com/css2?family=Lato:wght@700;900&display=swap">
<style>
  :root {
    --page-bg: #d2d2d4;
    --red: #f4120c;
    --red-orange: #ff4a0a;
    --orange: #ff7a00;
    --amber: #ffa200;
    --yellow: #ffd200;
    --band-yellow: #f7c400;
    --ink: #0a0a0a;
    --white: #ffffff;
    --dot-red: #e8101a;
    --label-border: #f2b400;
  }
  * { box-sizing: border-box; margin: 0; padding: 0; }
  html, body { width: 1200px; height: 1200px; overflow: hidden; }
  body {
    background: var(--page-bg);
    font-family: "Lato", Arial, sans-serif;
    position: relative;
  }
  .poster-frame {
    position: absolute;
    left: 136px;
    top: 0;
    width: 862px;
    height: 1116px;
    transform: scale(1.0753);
    transform-origin: top left;
  }
  .poster {
    position: relative;
    width: 862px;
    height: 1116px;
    overflow: hidden;
    background:
      radial-gradient(ellipse 420px 380px at 760px 1060px, var(--yellow) 0%, rgba(255,210,0,0) 100%),
      radial-gradient(ellipse 520px 420px at 420px 560px, var(--amber) 0%, rgba(255,162,0,0) 100%),
      linear-gradient(160deg, var(--red-orange) 0%, var(--orange) 45%, var(--orange) 70%, var(--red) 100%);
  }
  .headline {
    position: absolute;
    left: 0; right: 0; top: 12px;
    text-align: center;
    color: var(--white);
    font-weight: 900;
    font-size: 104px;
    letter-spacing: -1px;
    line-height: 1;
  }
  .role-band {
    position: absolute;
    left: 38px; top: 120px;
    width: 762px; height: 90px;
  }
  .role-title {
    position: absolute;
    left: 38px; top: 120px;
    width: 762px; height: 90px;
    display: flex; align-items: center; justify-content: center;
    color: var(--ink);
    font-weight: 900;
    font-size: 76px;
    letter-spacing: -0.5px;
    padding-left: 30px;
  }
  .bulb-photo {
    position: absolute;
    left: 258px; top: 388px;
    width: 355px; height: 620px;
    border-radius: 178px 178px 60px 60px / 200px 200px 60px 60px;
    background:
      radial-gradient(ellipse 160px 220px at 50% 45%, #fff200 0%, #ffe100 40%, rgba(255,190,0,0.6) 80%, rgba(255,160,0,0) 100%),
      linear-gradient(180deg, rgba(255,200,40,0.5) 0%, rgba(255,220,0,0.7) 60%, #4a3212 82%, #1e150a 100%);
  }
  .diagram {
    position: absolute;
    left: 0; top: 0;
    width: 862px; height: 1116px;
  }
  .unit-label {
    position: absolute;
    width: 142px; height: 34px;
    background: var(--ink);
    border: 2px solid var(--label-border);
    color: var(--white);
    font-weight: 900;
    font-size: 20px;
    display: flex; align-items: center; justify-content: center;
    letter-spacing: 0.3px;
  }
  .label-strom    { left: 360px; top: 240px; width: 147px; }
  .label-watt     { left: 16px;  top: 341px; }
  .label-ampere   { left: 701px; top: 341px; }
  .label-volt     { left: 18px;  top: 601px; width: 140px; }
  .label-ohm      { left: 701px; top: 601px; }
  .label-leistung { left: 18px;  top: 769px; font-size: 18px; }
  .label-spannung { left: 701px; top: 769px; font-size: 18px; }
  .mail-icon {
    position: absolute;
    left: 40px; top: 922px;
    width: 115px; height: 75px;
  }
  .apply-heading {
    position: absolute;
    left: 35px; top: 1012px;
    color: var(--white);
    font-weight: 900;
    font-size: 34px;
    line-height: 1;
  }
  .apply-email {
    position: absolute;
    left: 35px; top: 1052px;
    color: var(--white);
    font-weight: 700;
    font-size: 28px;
    line-height: 1;
  }
</style>
</head>
<body>
  <div class="poster-frame">
    <main class="poster">
      <h1 class="headline">WIR SUCHEN SIE!</h1>

      <svg class="role-band" viewBox="0 0 762 90" aria-hidden="true">
        <polygon points="52,0 762,0 715,90 0,90" fill="var(--band-yellow)"/>
      </svg>
      <h2 class="role-title">POWER WORKER</h2>

      <div class="bulb-photo" role="img" aria-label="Foto einer leuchtenden Glühbirne mit Schraubsockel"></div>

      <svg class="diagram" viewBox="0 0 862 1116" aria-hidden="true">
        <g fill="none" stroke="var(--white)">
          <path d="M298,785 C240,755 193,700 193,617 A240 281 0 0 1 673,617 C673,700 628,755 570,785" stroke-width="9" stroke-linecap="round"/>
          <g stroke-width="2">
            <line x1="433" y1="274" x2="433" y2="336"/>
            <polyline points="159,358 197,358 243,418"/>
            <polyline points="701,358 655,358 611,411"/>
            <line x1="158" y1="617" x2="193" y2="617"/>
            <line x1="673" y1="617" x2="701" y2="617"/>
            <line x1="160" y1="785" x2="298" y2="785"/>
            <line x1="570" y1="785" x2="701" y2="785"/>
          </g>
        </g>
        <g fill="var(--dot-red)" stroke="var(--white)" stroke-width="5">
          <circle cx="433" cy="336" r="13"/>
          <circle cx="243" cy="418" r="13"/>
          <circle cx="611" cy="411" r="13"/>
          <circle cx="193" cy="617" r="13"/>
          <circle cx="673" cy="617" r="13"/>
          <circle cx="298" cy="785" r="13"/>
          <circle cx="570" cy="785" r="13"/>
        </g>
      </svg>

      <div class="unit-label label-strom">STROM</div>
      <div class="unit-label label-watt">WATT</div>
      <div class="unit-label label-ampere">AMPERE</div>
      <div class="unit-label label-volt">VOLT</div>
      <div class="unit-label label-ohm">OHM</div>
      <div class="unit-label label-leistung">LEISTUNG</div>
      <div class="unit-label label-spannung">SPANNUNG</div>

      <svg class="mail-icon" viewBox="0 0 115 75" aria-hidden="true">
        <g stroke="var(--yellow)" stroke-linecap="round" fill="none">
          <line x1="8" y1="48" x2="14" y2="46" stroke-width="4"/>
          <line x1="4" y1="60" x2="16" y2="57" stroke-width="4"/>
          <line x1="14" y1="70" x2="30" y2="66" stroke-width="4"/>
          <g transform="rotate(-22 75 40)" stroke-width="5" stroke-linejoin="round">
            <rect x="42" y="18" width="68" height="44"/>
            <polyline points="42,18 76,44 110,18"/>
          </g>
        </g>
      </svg>

      <p class="apply-heading">BEWERBUNG AN:</p>
      <p class="apply-email">personal@elektro-brandt.de</p>
    </main>
  </div>
</body>
</html>
```